Cafe menu design

Hi there,

We need a editable menu layout and design to match our new cafe call: " Larkspur Fine Coffee", we love the ideas of A4 clip board and self print out menu in black and white. ( Example as attached)

We would like the menu can be break down into category easy for customer to flip around and read. ( example as attached)

Category including the following:

- All day breakfast and Sandwich and Toast
- Main (Lunch&Dinner) and Pizza
- Dessert snacks and nibbles
- Hot and Cold Drinks
- Catering menu

Please find our logo and our current menu as attached for your information and convenience.
Updates

Dear Designers, Thank you for your time and submission, Please find our drink menu and logo as attached. Kind Regards,

Target Market(s)

Young family, young Couple, office and corporate staff

Industry/Entity Type

Cafe

Font styles to use
Serif
Sans Serif

```html
<!DOCTYPE html>
<html lang="en">
<head>
<meta charset="UTF-8">
<title>Larkspur Fine Coffee — Dessert Snacks and Nibbles</title>
<link rel="stylesheet" href="https://fonts.googleapis.com/css2?family=Fira+Sans+Condensed:wght@300;400;700&display=swap">
<style>
  :root {
    --backdrop: #d9d6d7;
    --paper: #ffffff;
    --ink: #1e1e1e;
    --ink-soft: #555555;
    --ribbon: #3a3a3a;
    --ribbon-tail: #2a2a2a;
    --rule: #9a9a9a;
    --artwork: #e6e4e5;
  }
  * { box-sizing: border-box; margin: 0; padding: 0; }
  html, body { width: 1200px; height: 900px; overflow: hidden; }
  body {
    position: relative;
    background: var(--backdrop);
    font-family: "Fira Sans Condensed", "Arial Narrow", sans-serif;
    color: var(--ink);
  }
  .page {
    position: absolute;
    left: 251px;
    width: 653px;
    background: var(--paper);
    box-shadow: 3px 3px 4px rgba(0,0,0,0.35);
  }
  .page--next { top: 760px; height: 115px; }
  .page--dessert { top: 29px; height: 744px; }
  .page-shadow {
    position: absolute;
    left: 251px; top: 773px;
    width: 653px; height: 40px;
    background: linear-gradient(rgba(0,0,0,0.28), rgba(0,0,0,0));
  }
  .cover-artwork {
    position: absolute;
    left: 30px; top: 126px;
    width: 325px; height: 305px;
    background: radial-gradient(ellipse at 55% 45%, var(--artwork) 0%, var(--artwork) 45%, rgba(230,228,229,0) 72%);
  }
  .column-rule {
    position: absolute;
    left: 327px; top: 409px;
    height: 284px;
    border-left: 1px dotted var(--rule);
  }
  .footer-rule {
    position: absolute;
    left: 22px; width: 305px; height: 5px;
    background: repeating-linear-gradient(90deg, #bdbdbd 0 1px, transparent 1px 3px);
  }
  .page--dessert .footer-rule { top: 702px; }
  .page--next .footer-rule { top: 37px; }
  .page--next .column-rule { top: 20px; height: 8px; left: 325px; }
  .menu-list {
    position: absolute;
    left: 337px; top: 439px;
    width: 296px;
    list-style: none;
  }
  .menu-item { height: 39px; }
  .menu-item__line { display: flex; align-items: baseline; font-size: 11px; font-weight: 700; }
  .menu-item__leader { flex: 1; border-bottom: 1px dotted #b5b5b5; margin: 0 3px; }
  .menu-item__desc { font-size: 9.5px; font-weight: 300; color: var(--ink-soft); margin-top: 2px; }
  .section-ribbon { position: absolute; width: 296px; height: 34px; }
  .page--dessert .section-ribbon { left: 337px; top: 694px; }
  .page--next .section-ribbon { left: 335px; top: 30px; }
  .section-ribbon svg { position: absolute; inset: 0; }
  .section-ribbon__label {
    position: absolute; left: 33px; width: 232px; top: 0; height: 25px;
    line-height: 25px; text-align: center;
    color: #fff; font-size: 11px; font-weight: 700; letter-spacing: 0.2px;
  }
</style>
</head>
<body>
  <section class="page page--next">
    <div class="column-rule"></div>
    <div class="footer-rule"></div>
    <div class="section-ribbon">
      <svg viewBox="0 0 296 34" width="296" height="34">
        <polygon points="0,8 33,10 33,32 2,32 12,20" fill="var(--ribbon-tail)"/>
        <polygon points="296,8 263,10 263,32 294,32 284,20" fill="var(--ribbon-tail)"/>
        <rect x="33" y="0" width="232" height="25" fill="var(--ribbon)"/>
      </svg>
      <span class="section-ribbon__label">CATERING MENU</span>
    </div>
  </section>

  <div class="page-shadow"></div>

  <section class="page page--dessert">
    <div class="cover-artwork" role="img" aria-label="Faint grey illustration of a coffee tamper, portafilter and scattered coffee beans"></div>
    <div class="column-rule"></div>
    <ul class="menu-list">
      <li class="menu-item">
        <div class="menu-item__line"><span>Bread &amp; butter pudding</span><span class="menu-item__leader"></span><span>7</span></div>
        <p class="menu-item__desc">(Served warm with fresh cream)</p>
      </li>
      <li class="menu-item">
        <div class="menu-item__line"><span>Melting Belgian Chocolate Pudding</span><span class="menu-item__leader"></span><span>7</span></div>
        <p class="menu-item__desc">(Served warm with Ice Cream)</p>
      </li>
      <li class="menu-item">
        <div class="menu-item__line"><span>American brownie</span><span class="menu-item__leader"></span><span>7</span></div>
        <p class="menu-item__desc">&nbsp;(With fresh cream)</p>
      </li>
      <li class="menu-item">
        <div class="menu-item__line"><span>Honey pancake</span><span class="menu-item__leader"></span><span>15</span></div>
        <p class="menu-item__desc">(With golden maple syrup, fresh cut banana &amp; vanilla ice cream)</p>
      </li>
      <li class="menu-item">
        <div class="menu-item__line"><span>Belgian chocolate Waffles One/Two</span><span class="menu-item__leader"></span><span>6 / 10</span></div>
        <p class="menu-item__desc">(Crunchy Waffles with Belgian Chocolate Sauce)</p>
      </li>
      <li class="menu-item">
        <div class="menu-item__line"><span>Belgain chocolate Waffles &amp; Ice Cream One/Two</span><span class="menu-item__leader"></span><span>8.5 / 15</span></div>
        <p class="menu-item__desc">(Belgian Waffles, Fresh banana, Vanilla ice Cream Chocolate Sauce)</p>
      </li>
    </ul>
    <div class="footer-rule"></div>
    <div class="section-ribbon">
      <svg viewBox="0 0 296 34" width="296" height="34">
        <polygon points="0,8 33,10 33,32 2,32 12,20" fill="var(--ribbon-tail)"/>
        <polygon points="296,8 263,10 263,32 294,32 284,20" fill="var(--ribbon-tail)"/>
        <rect x="33" y="0" width="232" height="25" fill="var(--ribbon)"/>
      </svg>
      <span class="section-ribbon__label">DESSERT SNACKS AND NIBBLES</span>
    </div>
  </section>
</body>
</html>
```